Fast-casual chicken restaurant Brisket Barn needs a catering menu design

We need a catering menu designed for Brisket Barn. We are looking to design a 24x36in landscape menu board for our new catering menu. The catering memo attached includes our catering menu and Brisket Barn branding. More information about our brand can be found at https://brisketbarn-eats.example/.

```html
<!DOCTYPE html>
<html lang="en">
<head>
<meta charset="utf-8">
<title>Brisket Barn Catering Menu</title>
<link href="https://fonts.googleapis.com/css2?family=Montserrat:wght@400;500;700;800;900&display=swap" rel="stylesheet">
<style>
  :root {
    --red: #c9382a;
    --red-bar: #d2412b;
    --ink: #231f20;
    --cream: #fdf0d5;
    --white: #ffffff;
    --rule: #b9b2a6;
    --frame: #8d8780;
    --yellow: #f6c21c;
    --body: #2f2a27;
  }
  * { margin: 0; padding: 0; box-sizing: border-box; }
  html, body { width: 800px; height: 1200px; overflow: hidden; background: var(--white); }
  body { font-family: "Montserrat", Arial, sans-serif; color: var(--body); }
  .menu-board { position: relative; width: 800px; height: 1200px; background: var(--white); overflow: hidden; }

  .brand { position: absolute; left: 48px; top: 62px; display: flex; align-items: center; gap: 10px; }
  .brand-dot { width: 30px; height: 30px; border-radius: 50%; background: var(--red); }
  .brand-name { font-weight: 800; font-size: 30px; color: var(--yellow); letter-spacing: 0.5px; }

  .cream-panel { position: absolute; left: 0; top: 148px; width: 800px; height: 772px; background: var(--cream); }

  .food-shot { position: absolute; }
  .shot-wing-top { left: 378px; top: 24px; width: 140px; height: 160px; border-radius: 45% 55% 40% 60%; background: radial-gradient(circle at 45% 40%, #e8d59a, #b79450 75%); transform: rotate(-12deg); }
  .shot-tender { left: 565px; top: 52px; width: 175px; height: 170px; border-radius: 50% 45% 55% 40%; background: radial-gradient(circle at 50% 40%, #f0cf94, #c99251 75%); }
  .shot-wing-low { left: 612px; top: 252px; width: 118px; height: 118px; border-radius: 50% 40% 55% 45%; background: radial-gradient(circle at 50% 45%, #a0673a, #5b3219 80%); }
  .shot-dip { left: 490px; top: 306px; width: 82px; height: 78px; border-radius: 50%; background: radial-gradient(circle at 50% 45%, #f7f6f2, #d9d8d2 80%); }

  .headline { position: absolute; left: 58px; top: 204px; font-weight: 900; font-size: 92px; line-height: 76px; letter-spacing: 0.5px; }
  .headline .line-top { display: block; color: var(--red); }
  .headline .line-bottom { display: block; color: var(--ink); }

  .section { position: absolute; left: 62px; width: 670px; }
  .section-bar { background: var(--red-bar); color: var(--white); font-weight: 800; font-size: 15px; height: 25px; line-height: 25px; padding-left: 9px; letter-spacing: 0.3px; }
  .row { display: grid; grid-template-columns: 135px 78px 1fr 48px; height: 16px; line-height: 16px; font-size: 10.2px; border-bottom: 1px solid var(--rule); }
  .row.carte { grid-template-columns: 135px 1fr 48px; }
  .row .feeds { text-align: center; padding-right: 44px; }
  .row.head { color: var(--red); font-weight: 800; font-size: 11px; height: 21px; line-height: 24px; }
  .row.head .feeds { text-align: left; padding-right: 0; }

  .packaged { top: 398px; }
  .per-person { top: 495px; }
  .a-la-carte { top: 595px; }

  .flavour-box { position: absolute; left: 62px; top: 788px; width: 670px; height: 115px; border: 1px solid var(--frame); background: var(--white); display: grid; grid-template-columns: 155px 138px 123px 139px 1fr; }
  .flavour-col { border-right: 1px solid var(--frame); padding-top: 3px; }
  .flavour-col:last-child { border-right: none; }
  .flavour-col h3 { color: var(--red); font-weight: 800; font-size: 13px; padding: 0 10px 2px; border-bottom: 1px solid var(--frame); }
  .flavour-col ul { list-style: none; padding-top: 1px; }
  .flavour-col li { font-size: 10.2px; line-height: 17.6px; padding-left: 10px; white-space: nowrap; }

  .feast-photo { position: absolute; left: 0; top: 920px; width: 800px; height: 280px; background: linear-gradient(100deg, #7a4a2b 0%, #b9572e 35%, #c23a1d 55%, #9a5a32 80%, #5e3520 100%); }
  .site-url { position: absolute; right: 68px; top: 1146px; font-weight: 800; font-size: 21px; color: var(--yellow); text-decoration: none; }
</style>
</head>
<body>
<main class="menu-board">
  <div class="brand"><span class="brand-dot"></span><span class="brand-name">Brisket Barn</span></div>

  <div class="cream-panel"></div>

  <div class="food-shot shot-wing-top" role="img" aria-label="Garlic parmesan chicken wing"></div>
  <div class="food-shot shot-tender" role="img" aria-label="Breaded chicken tender"></div>
  <div class="food-shot shot-wing-low" role="img" aria-label="Dry-rubbed chicken wing"></div>
  <div class="food-shot shot-dip" role="img" aria-label="Cup of ranch dressing"></div>

  <h1 class="headline"><span class="line-top">CATERING</span><span class="line-bottom">MENU</span></h1>

  <section class="section packaged">
    <div class="section-bar">PACKAGED DEALS</div>
    <div class="row head"><span>NAME</span><span class="feeds">FEEDS</span><span>ITEMS</span><span>PRICE</span></div>
    <div class="row"><span>Family</span><span class="feeds">4</span><span>12 Tenders, sauces, dressing, large side, 2L</span><span>$24.99</span></div>
    <div class="row"><span>Tailgate</span><span class="feeds">10</span><span>20 Tenders, 30 wings, sauces, 2 party, dressings, 1 party side</span><span>$75.99</span></div>
    <div class="row"><span>House Party</span><span class="feeds">10</span><span>20 Tenders, 60 wings, sauces, 2 party sides, 2 party salads, dressings, 2 2L</span><span>$155.99</span></div>
  </section>

  <section class="section per-person">
    <div class="section-bar">PER PERSON DEALS</div>
    <div class="row head"><span>NAME</span><span class="feeds">FEEDS</span><span>ITEMS</span><span>PRICE</span></div>
    <div class="row"><span>Snack (per person)</span><span class="feeds">1</span><span>12 Tenders, sauce, dressing, large red side</span><span>$7.00</span></div>
    <div class="row"><span>Party (per person)</span><span class="feeds">1</span><span>2 Tenders, 3 wings, sauce, dressing, 1 reg side, 12oz/fountain drink</span><span>$11.00</span></div>
    <div class="row"><span>Feast (per person)</span><span class="feeds">1</span><span>2 Tenders, 6 wings, sauce, dressing, 1 reg side, dessert, 20oz drink</span><span>$15.00</span></div>
  </section>

  <section class="section a-la-carte">
    <div class="section-bar">A LA CARTE</div>
    <div class="row carte head"><span>ITEMS</span><span>INCREMENTS</span><span>PRICE</span></div>
    <div class="row carte"><span>Wings</span><span>50, 75, 100</span><span>$xx.xx</span></div>
    <div class="row carte"><span>Tenders</span><span>30, 45, 60</span><span>$xx.xx</span></div>
    <div class="row carte"><span>Waffle Fries</span><span>Party Size</span><span>$13.99</span></div>
    <div class="row carte"><span>Garlic Parm Tots</span><span>Party Size</span><span>$13.99</span></div>
    <div class="row carte"><span>Chicken Caesar Salad</span><span>Party Size</span><span>$38.99</span></div>
    <div class="row carte"><span>Caesar Salad</span><span>Party Size</span><span>$38.99</span></div>
    <div class="row carte"><span>Any Sauce</span><span>8oz</span><span>$1.99</span></div>
    <div class="row carte"><span>Cheese Sauce</span><span>8oz</span><span>$2.49</span></div>
  </section>

  <section class="flavour-box">
    <div class="flavour-col"><h3>FALVOURS</h3><ul><li>Honey Mustard</li><li>Hot Lemon Pepper</li><li>Jamaican Jerk</li><li>Mango Habanero</li><li>Sweet Chili</li></ul></div>
    <div class="flavour-col"><h3>BBQ</h3><ul><li>Cajun BBQ</li><li>Citrus Chipotle</li><li>Golden BBQ</li><li>Honey BBQ</li><li>Smoky BBQ</li></ul></div>
    <div class="flavour-col"><h3>DRY RUBS</h3><ul><li>7 Pepper</li><li>Cajun</li><li>Garlic Parm</li><li>Lemon Pepper</li><li>West Texas mesquite</li></ul></div>
    <div class="flavour-col"><h3>TERIYAKI</h3><ul><li>Cajun Teriyaki</li><li>Spicy Teriyaki</li><li>Traditional Teriyaki</li></ul></div>
    <div class="flavour-col"><h3>BUFFALO</h3><ul><li>Mild</li><li>Medium Heat</li><li>Hot Streak</li><li>Firecracker</li><li>Inferno</li></ul></div>
  </section>

  <div class="feast-photo" role="img" aria-label="Table spread of sauced chicken tenders, wings, waffle fries, celery and ribs with hands reaching in"></div>
  <a class="site-url" href="https://brisketbarn-eats.example/">brisketbarn-eats.example</a>
</main>
</body>
</html>
```